Vent doux

Hello,
I’m a designer sunglasses reatail Store owner in Montreal, Quebec.

Looking for something modern, fresh with a trendy appeal.

Will send my logo.
Thank you.

Store

```html
<!DOCTYPE html>
<html lang="fr">
<head>
<meta charset="utf-8">
<title>Vent doux – cartes d'affaires</title>
<link rel="stylesheet" href="https://fonts.googleapis.com/css2?family=Lato:wght@300;400;700&display=swap">
<style>
  :root {
    --backdrop: #3b3f47;
    --card-dark: #2b2b2c;
    --card-light: #ffffff;
    --brand-red: #9b1b30;
    --ink: #2a2a2a;
    --muted: #7a7a7a;
    --faint: rgba(255,255,255,0.07);
  }
  * { box-sizing: border-box; margin: 0; padding: 0; }
  html, body { width: 1200px; height: 900px; overflow: hidden; }
  body {
    background: var(--backdrop);
    font-family: "Lato", Arial, sans-serif;
    position: relative;
  }
  .card {
    position: absolute;
    width: 540px;
    height: 310px;
    overflow: hidden;
    box-shadow: 0 18px 40px rgba(0,0,0,0.45);
  }
  .card--front { left: 40px; top: 295px; background: var(--card-light); }
  .card--back { left: 620px; top: 295px; background: var(--card-dark); }

  /* front: light panel */
  .front-info { position: absolute; left: 0; top: 0; width: 290px; height: 100%; padding: 26px 0 0 26px; }
  .wordmark { display: flex; align-items: center; gap: 10px; }
  .wordmark__dot { width: 26px; height: 26px; border-radius: 50%; background: var(--brand-red); }
  .wordmark__name { font-size: 30px; font-weight: 700; color: var(--brand-red); letter-spacing: 1px; }
  .tagline {
    margin: 4px 0 0 36px;
    padding-top: 3px;
    width: 200px;
    border-top: 2px solid var(--brand-red);
    font-size: 12px; font-weight: 300; letter-spacing: 2.6px; color: var(--muted);
  }
  .address { margin-top: 30px; font-size: 14px; line-height: 18px; color: var(--ink); }
  .contacts { list-style: none; margin-top: 6px; font-size: 14px; line-height: 18px; color: var(--ink); }
  .contacts li { display: flex; align-items: center; gap: 7px; }
  .contacts svg { width: 11px; height: 11px; fill: var(--brand-red); flex: none; }

  /* front: dark panel */
  .front-identity { position: absolute; left: 290px; top: 0; width: 250px; height: 100%; background: var(--card-dark); }
  .holder { position: absolute; left: 30px; top: 28px; }
  .holder__name { font-size: 25px; color: var(--brand-red); letter-spacing: 0.5px; }
  .holder__role { font-size: 14px; font-weight: 300; color: #e8e8e8; margin-top: 2px; }
  .front-identity__mark {
    position: absolute; left: 26px; bottom: 56px;
    font-size: 34px; font-weight: 700; color: var(--faint); letter-spacing: 1px;
  }
  .edge-stripe {
    position: absolute; right: 0; top: 0; width: 18px; height: 100%;
    background: var(--card-light);
  }
  .edge-stripe::after {
    content: ""; position: absolute; left: 6px; top: 0; width: 3px; height: 100%;
    background: var(--brand-red);
  }

  /* back */
  .back-mark {
    position: absolute; inset: 0;
    display: flex; align-items: center; justify-content: center; gap: 14px;
  }
  .back-mark__dot { width: 40px; height: 40px; border-radius: 50%; background: var(--brand-red); }
  .back-mark__name { font-size: 46px; font-weight: 700; color: var(--brand-red); letter-spacing: 1px; }
</style>
</head>
<body>

<section class="card card--front" aria-label="Recto de la carte">
  <div class="front-info">
    <div class="wordmark">
      <span class="wordmark__dot"></span>
      <span class="wordmark__name">Vent doux</span>
    </div>
    <p class="tagline">lunettes &amp; accessoires</p>
    <p class="address">845 rue des Érables Est<br>Montreal (Qc) H3K 2B4</p>
    <ul class="contacts">
      <li><svg viewBox="0 0 16 16"><path d="M3 1l3 3-1.5 2c1 2 3 4 5 5l2-1.5 3 3-2 2C7 14 2 9 1 3z"/></svg>514 555-0142</li>
      <li><svg viewBox="0 0 16 16"><path d="M4 0h8v16H4zM5.5 2v10h5V2z"/></svg>514 555-0187</li>
      <li><svg viewBox="0 0 16 16"><path d="M0 3h16v10H0zM1.5 4.5L8 9l6.5-4.5z"/></svg>info@VentDoux.com</li>
      <li><svg viewBox="0 0 16 16"><circle cx="8" cy="8" r="7.5"/><path d="M0.5 8h15M8 0.5v15" stroke="#fff" stroke-width="1.2"/></svg>www.VentDoux.com</li>
    </ul>
  </div>
  <div class="front-identity">
    <div class="holder">
      <p class="holder__name">Julien Marchand</p>
      <p class="holder__role">Owner</p>
    </div>
    <span class="front-identity__mark" aria-hidden="true">Vent doux</span>
    <div class="edge-stripe"></div>
  </div>
</section>

<section class="card card--back" aria-label="Verso de la carte">
  <div class="back-mark">
    <span class="back-mark__dot"></span>
    <span class="back-mark__name">Vent doux</span>
  </div>
</section>

</body>
</html>
```